Design us a professional website for a Cannabis Staffing Agency

We already have a logo ready to go, but now we are looking for a few good web designs. We provide staffing for the Cannabis/Marijuana industry. We want a good balance of clean, simple and modern design but also embracing the exciting atmosphere of the Cannabis industry.

Here are examples of our competition, please note that most of these competitors design feel old and dated:

http://qrvplacementcrew.example/
https://tolbrix.example/tolbrix-main-page
http://saffronpathways.example/index.html
http://www.wickcrew.example/medical-marijuana-staffing-recruiting
http://www.tundrahiring.example/
www.placedupcrew.example
www.pinewise.example

I also would prefer an explanation of why you choose to design it the way you did? What was your thought process or did you use a template?

Requirements
Must have
• About Us Page
• Candidates Page
• Employer Page
• Job Opening Page
• Contact Us Page
Nice to have
• Colors to match the logo, good use of images and design to show the story. Our goal is to show our clients what we are about and not just tell them.

```html
<!DOCTYPE html>
<html lang="en">
<head>
<meta charset="utf-8">
<title>Verdanta — Cannabis Staffing</title>
<link href="https://fonts.googleapis.com/css2?family=Roboto:wght@400;500;700&family=Open+Sans:wght@400;600&display=swap" rel="stylesheet">
<style>
:root{
  --green:#5b9a0f;
  --green-dark:#4c820a;
  --ink:#222;
  --text:#666;
  --muted:#999;
  --line:#e3e3e3;
  --white:#fff;
  --slate:#5d5f60;
}
*{box-sizing:border-box;margin:0;padding:0}
html,body{width:1200px;height:2913px;overflow:hidden;background:var(--white)}
body{position:relative;font-family:"Open Sans",Arial,sans-serif;color:var(--text)}
.abs{position:absolute}
.heading{font-family:"Roboto",Arial,sans-serif;font-weight:700;color:var(--ink);text-transform:uppercase}

/* header */
.site-header{left:0;top:0;width:1200px;height:87px;background:var(--white);box-shadow:0 1px 4px rgba(0,0,0,.12);z-index:2}
.brand{left:97px;top:16px;display:flex;align-items:center;gap:12px}
.brand-dot{width:56px;height:56px;border-radius:50%;background:var(--green)}
.brand-name{font-family:"Roboto",sans-serif;font-weight:700;font-size:34px;color:var(--green);letter-spacing:1px}
.main-nav{left:366px;top:33px;display:flex;gap:25px;font-family:"Roboto",sans-serif;font-size:15px;font-weight:500;color:#333;text-transform:uppercase}
.main-nav .active{color:var(--green)}
.search-icon{left:970px;top:34px}
.login{left:1010px;top:25px;width:90px;height:38px;border:2px solid #aaa;color:var(--green);font-family:"Roboto",sans-serif;font-weight:700;font-size:15px;display:flex;align-items:center;justify-content:center;gap:6px}

/* hero */
.hero{left:0;top:87px;width:1200px;height:457px;background:linear-gradient(100deg,#4a4d55 0%,#8a8f98 35%,#c9c6c0 60%,#9b9ea6 100%)}
.hero-shade{left:0;top:87px;width:1200px;height:457px;background:rgba(20,25,30,.25)}
.hero-title{left:0;top:212px;width:1200px;text-align:center;font-family:"Roboto",sans-serif;font-weight:700;font-size:44px;color:var(--white);text-transform:uppercase}
.hero-sub{left:0;top:280px;width:1200px;text-align:center;font-size:20px;font-weight:600;color:var(--white)}
.btn{display:flex;align-items:center;justify-content:center;font-family:"Roboto",sans-serif;font-weight:700;text-transform:uppercase;color:var(--white)}
.btn-solid{background:var(--green)}
.btn-ghost{border:2px solid var(--white)}
.hero-btn{top:330px;height:54px;font-size:16px}
.dots{left:564px;top:469px;display:flex;gap:6px}
.dots span{width:14px;height:14px;border-radius:50%;border:2px solid var(--white)}
.dots span:first-child{background:var(--white)}

/* section titles */
.section-title{left:0;width:1200px;display:flex;justify-content:center;align-items:center;gap:16px;font-size:30px}
.title-mark{width:34px;height:34px;border-radius:50%;border:3px solid var(--green)}
.section-lede{left:250px;top:682px;width:700px;text-align:center;font-size:13.5px;line-height:26px;color:var(--text)}

/* feature cards */
.feature{top:781px;width:316px;height:266px;border:1px solid #ddd;box-shadow:0 1px 4px rgba(0,0,0,.08);text-align:center}
.feature svg{position:absolute;left:50%;transform:translateX(-50%);top:40px}
.feature h3{position:absolute;top:146px;width:100%;font-family:"Roboto",sans-serif;font-weight:500;font-size:20px;color:var(--ink)}
.feature p{position:absolute;top:184px;left:20px;right:20px;font-size:13.5px;line-height:25px}

/* split band */
.split{top:1140px;height:282px}
.split-cand{left:0;width:600px;background:linear-gradient(90deg,#6aa524,#7ab535)}
.split-emp{left:600px;width:600px;background:linear-gradient(90deg,#5a5c5e,#6c6e70)}
.split h2{position:absolute;top:48px;font-family:"Roboto",sans-serif;font-weight:700;font-size:30px;color:var(--white)}
.split p{position:absolute;top:96px;width:370px;font-size:13.5px;line-height:25px;color:var(--white)}
.split .btn{position:absolute;top:192px;height:48px;font-size:16px}
.split svg{position:absolute;top:28px}

/* blog */
.post{top:1581px;width:312px}
.post-photo{width:312px;height:212px}
.date-badge{position:absolute;left:-20px;top:140px;width:62px;height:64px}
.date-day{position:absolute;left:0;top:0;width:62px;height:32px;background:var(--green);color:var(--white);font-family:"Roboto",sans-serif;font-weight:700;font-size:19px;padding-left:10px;line-height:32px}
.date-mon{position:absolute;left:20px;top:32px;width:42px;height:28px;background:#3d3f41;color:var(--white);font-size:11px;font-weight:600;line-height:28px;text-align:center}
.post h3{position:absolute;top:232px;font-family:"Open Sans",sans-serif;font-weight:600;font-size:19px;color:var(--ink)}
.post p{position:absolute;top:266px;font-size:12.5px;line-height:23px}
.post hr{position:absolute;top:324px;width:312px;border:0;border-top:1px solid var(--line)}
.post-meta{position:absolute;top:341px;display:flex;gap:18px;font-size:12px;align-items:center}
.post-meta span{display:flex;gap:6px;align-items:center}

/* job search */
.jobs{left:0;top:2027px;width:1200px;height:313px;background:linear-gradient(95deg,#6b4a30 0%,#a47a55 30%,#3c4248 65%,#b88a6a 100%)}
.jobs-shade{left:0;top:2027px;width:1200px;height:313px;background:rgba(0,0,0,.25)}
.search-box{left:169px;top:2160px;width:860px;height:108px;background:rgba(70,60,55,.55)}
.field{display:flex;align-items:center;gap:8px;background:var(--white);font-size:13px;color:#777;padding-left:14px}
.search-box .field,.search-box .btn{position:absolute;top:34px;height:43px}

/* contact */
.col-title{font-family:"Roboto",sans-serif;font-weight:400;font-size:20px;color:var(--ink)}
.input{border:1px solid #bbb;font-size:12px;color:#777;padding:8px 14px}
.info-row{left:783px;display:flex;gap:20px;align-items:center;font-size:12.5px;line-height:22px}
.info-icon{width:36px;height:36px;border-radius:50%;border:1px solid #ddd;display:flex;align-items:center;justify-content:center;flex:none}
.socials{left:783px;top:2763px;display:flex;gap:9px}
.socials span{width:32px;height:32px;border-radius:50%}
.footer-line{left:97px;top:2830px;width:1004px;border-top:1px solid #ccc}
.copyright{left:0;top:2862px;width:1200px;text-align:center;font-size:12px;color:#666}
.to-top{left:1071px;top:2860px}
</style>
</head>
<body>

<header class="site-header abs">
  <div class="brand abs"><span class="brand-dot"></span><span class="brand-name">VERDANTA</span></div>
  <nav class="main-nav abs">
    <span class="active">Home</span><span>About Us</span><span>Candidates</span><span>Employer</span><span>Job Opening</span><span>Contact Us</span>
  </nav>
  <svg class="search-icon abs" width="18" height="18" viewBox="0 0 18 18"><circle cx="7" cy="7" r="5.5" fill="none" stroke="#333" stroke-width="2.2"/><line x1="11" y1="11" x2="16" y2="16" stroke="#333" stroke-width="2.6"/></svg>
  <div class="login abs"><svg width="12" height="14" viewBox="0 0 12 14"><rect x="1" y="6" width="10" height="8" fill="#5b9a0f"/><path d="M3 6V4a3 3 0 0 1 6 0v2" fill="none" stroke="#5b9a0f" stroke-width="2"/></svg>LOGIN</div>
</header>

<section>
  <div class="hero abs" role="img" aria-label="Photo of business people shaking hands across a meeting table"></div>
  <div class="hero-shade abs"></div>
  <h1 class="hero-title abs">Elevate Your Cannabis Career</h1>
  <p class="hero-sub abs">We provide staffing for the Cannabis/Marijuana industry</p>
  <a class="btn btn-solid hero-btn abs" style="left:402px;width:193px">Find Your Career</a>
  <a class="btn btn-ghost hero-btn abs" style="left:606px;width:192px">Find Great Talent</a>
  <div class="dots abs"><span></span><span></span><span></span><span></span></div>
</section>

<section>
  <h2 class="section-title heading abs" style="top:622px"><span class="title-mark"></span>Welcome to Verdanta</h2>
  <p class="section-lede abs">Nam libero tempore, cum soluta nobis est eligendi optio cumque nihil impedit quo minus id quod maxime placeat facere possimus, omnis voluptas assumenda est, omnis dolor repellendus.</p>

  <div class="feature abs" style="left:97px">
    <svg width="80" height="72" viewBox="0 0 80 72" fill="#5b9a0f">
      <circle cx="28" cy="42" r="18"/><circle cx="28" cy="42" r="7" fill="#fff"/>
      <g><rect x="24" y="18" width="8" height="8"/><rect x="24" y="58" width="8" height="8"/><rect x="4" y="38" width="8" height="8"/><rect x="44" y="38" width="8" height="8"/></g>
      <circle cx="60" cy="20" r="11"/><circle cx="60" cy="20" r="4" fill="#fff"/>
      <rect x="57" y="4" width="6" height="6"/><rect x="57" y="30" width="6" height="6"/><rect x="44" y="17" width="6" height="6"/><rect x="70" y="17" width="6" height="6"/>
    </svg>
    <h3>Improve Production</h3>
    <p>Nam libero tempore, cum soluta no bis est eligendi optio cumque nihil impe</p>
  </div>
  <div class="feature abs" style="left:443px">
    <svg width="80" height="64" viewBox="0 0 80 64" fill="#5b9a0f">
      <rect x="2" y="2" width="4" height="60"/><rect x="2" y="58" width="76" height="4"/>
      <rect x="14" y="26" width="10" height="28"/><rect x="30" y="36" width="10" height="18"/><rect x="46" y="22" width="10" height="32"/><rect x="62" y="30" width="10" height="24"/>
    </svg>
    <h3>Control Cost</h3>
    <p>Nam libero tempore, cum soluta no bis est eligendi optio cumque nihil impe</p>
  </div>
  <div class="feature abs" style="left:786px">
    <svg width="80" height="70" viewBox="0 0 80 70" fill="#5b9a0f">
      <circle cx="18" cy="16" r="9"/><circle cx="62" cy="16" r="9"/><circle cx="40" cy="14" r="12"/>
      <path d="M4 48a14 14 0 0 1 28 0z"/><path d="M48 48a14 14 0 0 1 28 0z"/>
      <path d="M20 66a20 20 0 0 1 40 0z"/><circle cx="40" cy="38" r="10"/>
    </svg>
    <h3>Manage Workers</h3>
    <p>Nam libero tempore, cum soluta no bis est eligendi optio cumque nihil impe</p>
  </div>
</section>

<section>
  <div class="split split-cand abs" role="img" aria-label="Green-tinted photo of a candidate working at a laptop">
    <svg style="left:100px" width="90" height="84" viewBox="0 0 80 70" fill="#fff">
      <circle cx="18" cy="16" r="9"/><circle cx="62" cy="16" r="9"/><circle cx="40" cy="14" r="12"/>
      <path d="M4 48a14 14 0 0 1 28 0z"/><path d="M48 48a14 14 0 0 1 28 0z"/>
      <path d="M20 66a20 20 0 0 1 40 0z"/><circle cx="40" cy="38" r="10"/>
    </svg>
    <h2 style="left:221px">CANDIDATES</h2>
    <p style="left:221px">At vero eos et accusamus et iusto odio dignissimos duci mus qui blanditiis praesentium voluptatum deleniti que corrupti quos dolores et quas mol.</p>
    <a class="btn btn-ghost" style="left:221px;width:192px">Find Your Career</a>
  </div>
  <div class="split split-emp abs" role="img" aria-label="Grey-tinted photo of an employer in an office">
    <svg style="left:54px" width="66" height="72" viewBox="0 0 66 72" fill="#fff">
      <circle cx="33" cy="20" r="18"/><path d="M2 72a31 28 0 0 1 62 0z"/>
    </svg>
    <h2 style="left:156px">EMPLOYER</h2>
    <p style="left:156px">At vero eos et accusamus et iusto odio dignissimos duci mus qui blanditiis praesentium voluptatum deleniti que corrupti quos dolores et quas mol.</p>
    <a class="btn btn-ghost" style="left:156px;width:190px">Find Great Talent</a>
  </div>
</section>

<section>
  <h2 class="section-title heading abs" style="top:1502px"><span class="title-mark"></span>Verdanta Blog</h2>

  <article class="post abs" style="left:97px">
    <div class="post-photo" role="img" aria-label="Photo of a man smiling at his laptop in an office" style="background:linear-gradient(120deg,#c9d6e3,#7d93ab 55%,#e6e9ee)"></div>
    <div class="date-badge"><div class="date-day">02</div><div class="date-mon">AUG</div></div>
    <h3>Finibus Bonorum et Malorum</h3>
    <p>Nam libero tempore, cum soluta nobis est eligendi optio cumque nihil impedit quo minus id qu..</p>
    <hr>
    <div class="post-meta"><span><svg width="11" height="12" viewBox="0 0 11 12" fill="#5b9a0f"><circle cx="5.5" cy="3.5" r="3.2"/><path d="M0 12a5.5 5 0 0 1 11 0z"/></svg>Sam Ortiz</span><span><svg width="14" height="11" viewBox="0 0 14 11" fill="none" stroke="#5b9a0f" stroke-width="1.6"><ellipse cx="7" cy="5" rx="6" ry="4"/></svg>3 Comments</span></div>
  </article>
  <article class="post abs" style="left:443px">
    <div class="post-photo" role="img" aria-label="Photo of a hand writing on a form beside a small potted plant" style="background:linear-gradient(120deg,#8a9a6a,#dcdcd6 50%,#f3f3f1)"></div>
    <div class="date-badge"><div class="date-day">02</div><div class="date-mon">AUG</div></div>
    <h3>Finibus Bonorum et Malorum</h3>
    <p>Nam libero tempore, cum soluta nobis est eligendi optio cumque nihil impedit quo minus id qu..</p>
    <hr>
    <div class="post-meta"><span><svg width="11" height="12" viewBox="0 0 11 12" fill="#5b9a0f"><circle cx="5.5" cy="3.5" r="3.2"/><path d="M0 12a5.5 5 0 0 1 11 0z"/></svg>Sam Ortiz</span><span><svg width="14" height="11" viewBox="0 0 14 11" fill="none" stroke="#5b9a0f" stroke-width="1.6"><ellipse cx="7" cy="5" rx="6" ry="4"/></svg>3 Comments</span></div>
  </article>
  <article class="post abs" style="left:789px">
    <div class="post-photo" role="img" aria-label="Photo of a team meeting around a conference table" style="background:linear-gradient(120deg,#e4e6ea,#8e939c 55%,#d6d8dc)"></div>
    <div class="date-badge"><div class="date-day">02</div><div class="date-mon">AUG</div></div>
    <h3>Finibus Bonorum et Malorum</h3>
    <p>Nam libero tempore, cum soluta nobis est eligendi optio cumque nihil impedit quo minus id qu..</p>
    <hr>
    <div class="post-meta"><span><svg width="11" height="12" viewBox="0 0 11 12" fill="#5b9a0f"><circle cx="5.5" cy="3.5" r="3.2"/><path d="M0 12a5.5 5 0 0 1 11 0z"/></svg>Sam Ortiz</span><span><svg width="14" height="11" viewBox="0 0 14 11" fill="none" stroke="#5b9a0f" stroke-width="1.6"><ellipse cx="7" cy="5" rx="6" ry="4"/></svg>3 Comments</span></div>
  </article>
</section>

<section>
  <div class="jobs abs" role="img" aria-label="Blurred photo of a person using a tablet"></div>
  <div class="jobs-shade abs"></div>
  <h2 class="section-title heading abs" style="top:2088px;color:#fff"><span class="title-mark" style="border-color:#fff"></span>Job Opening</h2>
  <div class="search-box abs">
    <div class="field" style="left:29px;width:301px"><svg width="12" height="12" viewBox="0 0 18 18"><circle cx="7" cy="7" r="5.5" fill="none" stroke="#555" stroke-width="2.4"/><line x1="11" y1="11" x2="16" y2="16" stroke="#555" stroke-width="2.8"/></svg>Keyword, Job Title or Company</div>
    <div class="field" style="left:344px;width:301px"><svg width="10" height="13" viewBox="0 0 10 14"><path d="M5 0a5 5 0 0 1 5 5c0 4-5 9-5 9S0 9 0 5a5 5 0 0 1 5-5z" fill="#555"/><circle cx="5" cy="5" r="2" fill="#fff"/></svg>City, State or Zip</div>
    <a class="btn btn-solid" style="left:664px;width:169px;font-size:15px;gap:8px"><svg width="13" height="13" viewBox="0 0 13 13" fill="#fff"><path d="M0 13l1-4 8-8 3 3-8 8z"/></svg>Apply Today</a>
  </div>
</section>

<section>
  <h2 class="section-title heading abs" style="top:2426px"><span class="title-mark"></span>Contact Us</h2>

  <h3 class="col-title abs" style="left:97px;top:2505px">Contact form</h3>
  <div class="input abs" style="left:99px;top:2569px;width:311px;height:33px">Name :</div>
  <div class="input abs" style="left:418px;top:2569px;width:310px;height:33px">Phone no :</div>
  <div class="input abs" style="left:99px;top:2616px;width:629px;height:31px">Email :</div>
  <div class="input abs" style="left:99px;top:2660px;width:629px;height:82px">Message :</div>
  <a class="btn btn-solid abs" style="left:623px;top:2760px;width:105px;height:35px;font-size:14px">Submit</a>

  <h3 class="col-title abs" style="left:783px;top:2505px">Contact Information</h3>
  <div class="info-row abs" style="top:2557px">
    <span class="info-icon"><svg width="10" height="14" viewBox="0 0 10 14"><path d="M5 0a5 5 0 0 1 5 5c0 4-5 9-5 9S0 9 0 5a5 5 0 0 1 5-5z" fill="#5b9a0f"/><circle cx="5" cy="5" r="2" fill="#fff"/></svg></span>
    <span>PO Box 41220 Marlow Lane 318,<br>Cedar Falls, IA</span>
  </div>
  <div class="info-row abs" style="top:2613px">
    <span class="info-icon"><svg width="13" height="13" viewBox="0 0 14 14"><path d="M3 0l3 3-2 2a9 9 0 0 0 5 5l2-2 3 3-2 3C6 14 0 8 0 3z" fill="#5b9a0f"/></svg></span>
    <span>1 555 014 2290</span>
  </div>
  <div class="info-row abs" style="top:2664px">
    <span class="info-icon"><svg width="14" height="11" viewBox="0 0 14 11"><rect width="14" height="11" rx="1" fill="#5b9a0f"/><path d="M0 1l7 5 7-5" fill="none" stroke="#fff" stroke-width="1.4"/></svg></span>
    <span>info@verdanta.example</span>
  </div>

  <h3 class="col-title abs" style="left:783px;top:2718px">Social Media</h3>
  <div class="socials abs" aria-label="Social media links">
    <span style="background:#3b5998"></span><span style="background:#2aa3ef"></span><span style="background:#0e76a8"></span><span style="background:#cb2027"></span>
  </div>

  <div class="footer-line abs"></div>
  <p class="copyright abs">Copyright © 2017, Verdanta. All rights reserved.</p>
  <svg class="to-top abs" width="30" height="18" viewBox="0 0 30 18"><path d="M2 16L15 3l13 13" fill="none" stroke="#999" stroke-width="3"/></svg>
</section>

</body>
</html>
```